Velora Botanics- New and unique line of Pet Products

Hi,

Velora Botanics is a manufacturer of natural products.

We need fresh and creative labels, for our new pet care product line:
- Specially scented for male- dog shampoo called "Ranger"
- Specially scented for female- dog shampoo called "Velvet paws"
- Cat cleaning wipes
- Stain and odor remover (for pet urine)

For more info on the products:
Velorabotanics.com
(please don't rely on the current labels for the pet products)

ATTACHED- you will find 2 products from Shopvale, which we like the design, as an example.

Best wishes,
Tomas
Velora Botanicsâ„¢
Updates

Project Deadline Extended
Reason: I did a vote, No one is very excited about the current designs Im not sure what to do next
Added Wednesday, August 24, 2016

Target Market(s)

Designed for pet owners and pet grooming professionals.

Industry/Entity Type

Pet Care

Requirements
Must have
• - The label should have a common language between products; same them, that can be modified to all products by change of writing and picture.
• - Reflects the natural aspect of the company & products, safe for the children and pets, was NOT tested on animals
• - Unique feature of the product (one destined for male dogs, other for female, the third for cats)
• Attached company Logo (Velora Botanicsâ„¢); should appear on the label.
• - Emphasize the difference for male / female dogs.
Nice to have
• - Maybe cartoon of a family bathing the male dog / female dog / cat - ?
• I think that the common feature should be a cartoon of a pet owner/s with different pets
• Made in the USA
• - Bottles are white
• - Dimensions:
• Male dog / Female dog / Odor & stain - 6"x7" & 4.25"x11"
• Cat: 4.5"x2.5" front & back
Should not have
• Please don't use stock images;
• We do private label and cannot have similar photos as our customers, must be unique.

```html
<!DOCTYPE html>
<html lang="en">
<head>
<meta charset="UTF-8">
<title>Velora Botanics – Oatmeal Pet Shampoo Labels</title>
<link href="https://fonts.googleapis.com/css2?family=Fredoka:wght@700&family=Roboto+Condensed:wght@400;700&family=Cabin:wght@400;600&family=Roboto:wght@400&display=swap" rel="stylesheet">
<style>
  :root {
    --bg: #ffffff;
    --purple: #b24fd0;
    --purple-deep: #8a34b3;
    --green: #6cc24a;
    --green-deep: #4fa934;
    --brand-green: #5fbf3f;
    --brand-grey: #6d6e70;
    --white: #ffffff;
    --water: #bff3f6;
  }
  * { margin: 0; padding: 0; box-sizing: border-box; }
  html, body { width: 1200px; height: 1200px; overflow: hidden; background: var(--bg); }
  .canvas { position: relative; width: 1200px; height: 1200px; }

  .label {
    position: absolute; top: 318px; width: 272px; height: 718px;
    color: var(--white); text-align: center;
  }
  .label--velvet { left: 194px; background: linear-gradient(180deg, var(--purple-deep) 0%, var(--purple) 45%, var(--purple-deep) 100%); --accent: var(--purple-deep); }
  .label--ranger { left: 579px; background: linear-gradient(180deg, var(--green-deep) 0%, var(--green) 45%, var(--green-deep) 100%); --accent: var(--green-deep); }

  .brand-badge {
    position: absolute; left: 14px; top: 26px; width: 144px; height: 144px;
    border-radius: 50%; background: var(--white); border: 3px solid var(--brand-green);
    display: flex; align-items: center; justify-content: center;
    font-family: "Cabin", sans-serif; font-weight: 400; font-size: 19px; line-height: 1.15;
    color: var(--brand-green); padding: 18px;
  }

  .illustration {
    position: absolute; left: 22px; top: 160px; width: 228px; height: 190px;
    border-radius: 10px 10px 40px 40px;
  }
  .label--velvet .illustration { background: linear-gradient(180deg, #f4eef8 0%, #ffffff 55%, var(--water) 100%); }
  .label--ranger .illustration { background: linear-gradient(180deg, #c98a3a 0%, #d0eaa0 60%, #e6f5c4 100%); }

  .product-name {
    position: absolute; left: 0; right: 0; top: 360px;
    font-family: "Fredoka", sans-serif; font-weight: 700; line-height: 1;
    text-shadow: 0 2px 0 rgba(0,0,0,0.12);
  }
  .label--velvet .product-name { font-size: 40px; top: 368px; }
  .label--ranger .product-name { font-family: "Roboto Condensed", sans-serif; font-size: 56px; letter-spacing: 1px; }

  .banner {
    position: absolute; left: 36px; width: 200px; top: 426px; height: 28px;
    background: var(--white); color: var(--accent);
    clip-path: polygon(8% 0, 92% 0, 100% 50%, 92% 100%, 8% 100%, 0 50%);
    font-family: "Roboto Condensed", sans-serif; font-size: 15px; line-height: 28px;
  }

  .features {
    position: absolute; left: 0; right: 0; top: 470px;
    font-family: "Cabin", sans-serif; font-weight: 600; font-size: 13px; line-height: 17px;
  }
  .rule { position: absolute; left: 48px; width: 180px; top: 528px; height: 2px; background: var(--white); }
  .slogan {
    position: absolute; left: 0; right: 0; top: 540px;
    font-family: "Cabin", sans-serif; font-weight: 600; font-size: 15px;
  }
  .ingredients {
    position: absolute; left: 0; right: 0; top: 578px;
    font-family: "Cabin", sans-serif; font-weight: 400; font-size: 12px; line-height: 17px;
  }
  .net {
    position: absolute; left: 0; right: 0; top: 665px;
    font-family: "Roboto", sans-serif; font-size: 13px;
  }

  .brand-lockup {
    position: absolute; left: 896px; top: 582px;
    display: flex; align-items: center; gap: 12px;
    font-family: "Cabin", sans-serif; font-weight: 400; font-size: 34px; color: var(--brand-green);
  }
  .brand-lockup__dot { width: 20px; height: 20px; border-radius: 50%; background: var(--brand-green); }
</style>
</head>
<body>
<main class="canvas">

  <section class="label label--velvet">
    <div class="brand-badge">Velora Botanics</div>
    <div class="illustration" role="img" aria-label="Cartoon of a small white fluffy dog bathing in a tub with bubbles"></div>
    <h1 class="product-name">Velvet Paws</h1>
    <div class="banner">OATMEAL PET SHAMPOO</div>
    <p class="features">• Deodorizing • PH balanced •<br>• Pure &amp; Natural •<br>• Super Concentrated •</p>
    <div class="rule"></div>
    <p class="slogan">Specially Scented for your Ranger!</p>
    <p class="ingredients">Aloe vera<br>Chamomile Extract<br>Vitamin E</p>
    <p class="net">Net Contents: 16FL. OZ. (472 ML)</p>
  </section>

  <section class="label label--ranger">
    <div class="brand-badge">Velora Botanics</div>
    <div class="illustration" role="img" aria-label="Cartoon of a golden retriever bathing in a green tub with bubbles"></div>
    <h1 class="product-name">RANGER</h1>
    <div class="banner">OATMEAL PET SHAMPOO</div>
    <p class="features">• Deodorizing • PH balanced •<br>• Pure &amp; Natural •<br>• Super Concentrated •</p>
    <div class="rule"></div>
    <p class="slogan">Specially Scented for your Ranger!</p>
    <p class="ingredients">Aloe vera<br>Chamomile Extract<br>Vitamin E</p>
    <p class="net">Net Contents: 16FL. OZ. (472 ML)</p>
  </section>

  <div class="brand-lockup">
    <span class="brand-lockup__dot"></span>
    <span>Velora Botanics</span>
  </div>

</main>
</body>
</html>
```